Garage Flooring Flyer

We are looking for a flyer design for our garage flooring company. We specialise in installing garage floor coatings. We use industrial grade products and are serious about durability and quality.
We target male car enthusiasts and want to project the image of a modern high-tech company. The flyer should be stunningly visual and incorporate the logo and photos we have attached. Other photos or images are welcomed.
Some key mentions to be made on the flyer are listed below:
About Us
"We are K*** R***** LLC, Home of the garage enthusiasts and Waukesha’s premier garage floor installer"
Services
Garage Floor Coatings
Offers
-Call or Email for a FREE estimate!
Credentials
-QN logo
-Pictavo Logo
-Zorbin Logo
-5stars?
Benefit Highlights to be mentioned or listed (not in any particular order)
-Industrial Quality and Strength
-Easy to Clean
-Many Color Options
-Locally Owned and Operated
-Satisfaction Guaranteed
-Lifetime Limited Warranty
-Increases Home Value
-MAKE YOUR FRIENDS AND NEIGHBORS JEALOUS!
-Fully Insured
-Certified and Trusted Installer
-Oil and Chemical Resistant
-UV Stable
-Impact and Abrasion Resistant
Contact Info
-Phone
-Email
-Website
Captions
-"From diamond grinding surface prep to using only the highest industrial-grade products, we believe in taking the time to ensure a proper installation and guarantee a durable long-lasting and beautiful garage floor";
-Serving Southeastern Wisconsin!

```html
<!DOCTYPE html>
<html lang="en">
<head>
<meta charset="utf-8">
<title>Torq Garage – Garage Floor Coating Flyers</title>
<link rel="stylesheet" href="https://fonts.googleapis.com/css2?family=Oswald:wght@500;600;700&family=Ubuntu:wght@400;500;700&display=swap">
<style>
  :root{
    --crimson:#8c0f2a;
    --crimson-dark:#5a0518;
    --ink:#1a1a1a;
    --charcoal:#1f1f22;
    --paper:#f3f3f3;
    --mist:#e4e4e4;
    --stage:#8d8d8d;
    --white:#ffffff;
  }
  *{box-sizing:border-box;margin:0;padding:0}
  html,body{width:1200px;height:1200px;overflow:hidden}
  body{background:var(--stage);font-family:"Ubuntu",sans-serif;position:relative}
  .page{position:absolute;width:557px;height:720px;background:var(--paper);overflow:hidden;box-shadow:0 6px 18px rgba(0,0,0,.35)}
  .page--front{left:24px;top:44px}
  .page--back{left:620px;top:404px;width:554px}
  .abs{position:absolute}
  .photo{position:absolute}
  .heading{font-family:"Oswald",sans-serif;font-weight:700;text-transform:uppercase;letter-spacing:-.2px}

  /* front */
  .brand{left:19px;top:26px;font-family:"Ubuntu",sans-serif;font-weight:700;font-size:34px;color:var(--ink);letter-spacing:2px;display:flex;align-items:center;gap:10px}
  .phone-tab{left:304px;top:14px;width:253px;height:62px;border-radius:12px 0 0 12px;background:linear-gradient(180deg,#a8163a,var(--crimson-dark));display:flex;align-items:center;gap:12px;padding-left:20px;color:var(--white);font-size:26px;font-weight:500;box-shadow:0 2px 4px rgba(0,0,0,.3)}
  .phone-tab__icon{width:38px;height:38px;background:var(--white);border-radius:9px;display:flex;align-items:center;justify-content:center}
  .hero{left:0;top:92px;width:557px;height:276px;background:linear-gradient(120deg,#1d2145 0%,#3a3f66 30%,#9a9ea6 55%,#c9cbcf 100%)}
  .intro-panel{left:306px;top:92px;width:251px;height:276px;background:rgba(24,24,26,.93);color:var(--white);padding:36px 10px 0 14px}
  .intro-panel__about{font-size:17px;line-height:20px;font-weight:600;letter-spacing:-.3px}
  .intro-panel__offer{font-size:20px;line-height:25px;margin-top:22px;white-space:nowrap;font-weight:600;letter-spacing:-.3px}
  .lower-field{left:0;top:368px;width:557px;height:232px;background:linear-gradient(180deg,#d8d8d8,#f4f4f4 40%,#e9e9e9)}
  .swatch{width:92px;height:92px;transform:rotate(45deg);background:var(--crimson);border:3px solid var(--crimson-dark);box-shadow:0 4px 8px rgba(0,0,0,.35)}
  .swatch__chip{position:absolute;inset:9px;border:3px solid var(--white)}
  .serving{left:0;top:458px;width:557px;text-align:center;font-size:27px;color:var(--ink);white-space:nowrap}
  .about-copy{left:24px;top:502px;width:509px;text-align:center;font-size:14.5px;line-height:19.5px;color:var(--ink)}
  .estimate-band{left:0;top:600px;width:557px;height:70px;background:linear-gradient(180deg,#c4c4c4,#a9a9a9);border-top:3px solid var(--crimson);display:flex;align-items:center;justify-content:center;font-size:30px;color:var(--ink);white-space:nowrap;letter-spacing:-.4px}
  .footer{position:absolute;left:0;bottom:0;width:100%;height:50px;background:linear-gradient(180deg,#a0123a,var(--crimson-dark));color:var(--white);display:flex;align-items:center;justify-content:center;gap:28px;font-size:16px;font-weight:500}
  .footer span{display:flex;align-items:center;gap:5px}

  /* back */
  .showroom{left:0;top:0;width:554px;height:290px;background:linear-gradient(180deg,#b9bcc0 0%,#e8e9ea 20%,#d4d5d6 60%,#8d8e90 100%)}
  .showroom__fade{left:0;top:250px;width:554px;height:60px;background:linear-gradient(180deg,rgba(243,243,243,0),var(--paper))}
  .accent-bar{left:0;top:28px;width:14px;height:136px;background:var(--crimson)}
  .jealous{left:14px;top:66px;width:262px;text-align:center;font-size:25px;line-height:30px;color:var(--crimson);white-space:nowrap;letter-spacing:-.5px;font-weight:600}
  .checks{list-style:none;font-weight:500;color:var(--ink)}
  .checks li{display:flex;align-items:center;gap:5px;white-space:nowrap}
  .checks--top{left:304px;top:50px;font-size:16px}
  .checks--top li{height:22px}
  .checks--benefits{left:32px;top:478px;font-size:16px;font-weight:700}
  .checks--benefits li{height:25.6px}
  .framed{position:absolute;border:5px solid var(--white);box-shadow:0 2px 6px rgba(0,0,0,.3)}
  .benefits-title{left:18px;top:424px;font-family:"Oswald",sans-serif;font-weight:600;color:var(--crimson);font-size:26px;font-variant:small-caps;text-transform:none;border-bottom:3px solid var(--crimson);padding-bottom:1px}
  .reviews{left:340px;top:640px;width:200px;display:flex;align-items:center;justify-content:space-between;font-size:15px;font-weight:500;color:var(--crimson)}
  .reviews__stars{letter-spacing:-1px;font-size:14px}
  .page--back .footer{gap:26px;font-size:15.5px}
</style>
</head>
<body>

<svg width="0" height="0" style="position:absolute">
  <defs>
    <symbol id="tick" viewBox="0 0 14 14"><path d="M1 8 L5 12 L13 2" fill="none" stroke="#8c0f2a" stroke-width="2.6" stroke-linecap="round" stroke-linejoin="round"/></symbol>
    <symbol id="mail" viewBox="0 0 16 12"><rect x="0" y="0" width="16" height="12" fill="#fff"/><path d="M0 0 L8 7 L16 0" fill="none" stroke="#8c0f2a" stroke-width="1.5"/></symbol>
    <symbol id="globe" viewBox="0 0 16 16"><g fill="none" stroke="#fff" stroke-width="1.4"><circle cx="8" cy="8" r="7"/><ellipse cx="8" cy="8" rx="3" ry="7"/><path d="M1 8h14M2.5 4.5h11M2.5 11.5h11"/></g></symbol>
    <symbol id="handset" viewBox="0 0 12 18"><rect x="1" y="1" width="10" height="16" rx="2" fill="none" stroke="currentColor" stroke-width="1.8"/><rect x="4.5" y="13.5" width="3" height="1.5" fill="currentColor"/></symbol>
  </defs>
</svg>

<!-- Front flyer -->
<section class="page page--front">
  <div class="abs brand"><span>TORQ GARAGE</span></div>
  <div class="abs phone-tab">
    <span class="phone-tab__icon" style="color:var(--crimson)"><svg width="16" height="24"><use href="#handset"/></svg></span>
    123-456-7809
  </div>

  <div class="photo hero" role="img" aria-label="Navy sports car parked on a grey flake-coated garage floor with white cabinets and wall storage"></div>
  <div class="abs intro-panel heading">
    <p class="intro-panel__about">We are K*** R***** LLC, home of the garage enthusiasts and Waukesha’s premier garage floor installer</p>
    <p class="intro-panel__offer">We offer<br>garage floor coatings</p>
  </div>

  <div class="abs lower-field" role="img" aria-label="Bright empty garage interior with a freshly coated floor"></div>

  <div class="abs swatch" style="left:38px;top:322px"><div class="swatch__chip" role="img" aria-label="Black and white flake floor sample" style="background:linear-gradient(135deg,#2b2b2b,#8a8a8a)"></div></div>
  <div class="abs swatch" style="left:168px;top:322px"><div class="swatch__chip" role="img" aria-label="Tan and brown flake floor sample" style="background:linear-gradient(135deg,#a49072,#d8ccb4)"></div></div>
  <div class="abs swatch" style="left:298px;top:322px"><div class="swatch__chip" role="img" aria-label="Beige and cream flake floor sample" style="background:linear-gradient(135deg,#9c8361,#cfb895)"></div></div>
  <div class="abs swatch" style="left:428px;top:322px"><div class="swatch__chip" role="img" aria-label="Grey and slate flake floor sample" style="background:linear-gradient(135deg,#5e6466,#a4aaa9)"></div></div>

  <h2 class="abs serving heading">Serving Southeastern Wisconsin !</h2>
  <p class="abs about-copy">From diamond grinding surface prep to using only the highest industrial-grade products, we believe in taking the time to ensure a proper installation and guarantee a durable long-lasting and beautiful garage floor</p>

  <div class="abs estimate-band heading">Call or email for a free estimate !</div>

  <footer class="footer">
    <span><svg width="18" height="13"><use href="#mail"/></svg>info@yourmail.com</span>
    <span><svg width="17" height="17"><use href="#globe"/></svg>www.yourcompany.com</span>
  </footer>
</section>

<!-- Back flyer -->
<section class="page page--back">
  <div class="photo showroom" role="img" aria-label="Large showroom garage with a white muscle car on a lift, a dark coupe and a wooden workbench on a speckled grey floor"></div>
  <div class="abs showroom__fade"></div>
  <div class="abs accent-bar"></div>
  <h2 class="abs jealous heading">Make your friends and<br>neighbors jealous!</h2>

  <ul class="abs checks checks--top">
    <li><svg width="14" height="14"><use href="#tick"/></svg>Fully Insured</li>
    <li><svg width="14" height="14"><use href="#tick"/></svg>Certified and Trusted Installer</li>
    <li><svg width="14" height="14"><use href="#tick"/></svg>Oil and Chemical Resistant</li>
    <li><svg width="14" height="14"><use href="#tick"/></svg>UV Stable</li>
    <li><svg width="14" height="14"><use href="#tick"/></svg>Impact and Abrasion Resistant</li>
  </ul>

  <div class="framed" style="left:20px;top:276px;width:250px;height:128px;background:linear-gradient(160deg,#d9dadc,#6c7480 55%,#8d97a3)" role="img" aria-label="Grey sports car on a blue-grey flake floor"></div>
  <div class="framed" style="left:180px;top:358px;width:134px;height:98px;background:linear-gradient(180deg,#2a2a2c 0%,#3b3b3d 55%,#c9c6c2 70%,#e3e0dc)" role="img" aria-label="Black supercar on a light coated floor"></div>
  <div class="framed" style="left:330px;top:242px;width:208px;height:124px;background:linear-gradient(180deg,#8f9296 0%,#b7b9bc 45%,#c9cacb 60%,#a9aaab)" role="img" aria-label="White car beside grey cabinetry on a coated floor"></div>
  <div class="framed" style="left:330px;top:378px;width:208px;height:125px;background:linear-gradient(180deg,#d7d3cc 0%,#6e706e 40%,#bfbfbd 75%,#9d9e9c)" role="img" aria-label="Garage with grey cabinets and a black sports car"></div>
  <div class="framed" style="left:330px;top:512px;width:208px;height:122px;background:linear-gradient(180deg,#e4e2de 0%,#cfccc6 60%,#707174 80%,#8c8d8f)" role="img" aria-label="Bright garage with bicycles on the wall and a dark coated floor"></div>

  <h3 class="abs benefits-title">Benefits</h3>
  <ul class="abs checks checks--benefits">
    <li><svg width="14" height="14"><use href="#tick"/></svg>Industrial Quality and Strength</li>
    <li><svg width="14" height="14"><use href="#tick"/></svg>Easy to Clean</li>
    <li><svg width="14" height="14"><use href="#tick"/></svg>Many Color Options</li>
    <li><svg width="14" height="14"><use href="#tick"/></svg>Locally Owned and Operated</li>
    <li><svg width="14" height="14"><use href="#tick"/></svg>Satisfaction Guaranteed</li>
    <li><svg width="14" height="14"><use href="#tick"/></svg>Lifetime Limited Warranty</li>
    <li><svg width="14" height="14"><use href="#tick"/></svg>Increases Home Value</li>
  </ul>

  <div class="abs reviews">
    <span>QN</span>
    <span>Pictavo</span>
    <span>Zorbin</span>
    <span class="reviews__stars">★★★★★</span>
  </div>

  <footer class="footer">
    <span><svg width="18" height="13"><use href="#mail"/></svg>info@yourmail.com</span>
    <span><svg width="17" height="17"><use href="#globe"/></svg>www.yourcompany.com</span>
    <span style="color:var(--white);font-size:14.5px"><svg width="11" height="16"><use href="#handset"/></svg>123-456-7809</span>
  </footer>
</section>

</body>
</html>
```